Landing Page for Bathroom Remodeling Webpage - Desktop and Mobile

I am looking for some help designing the "above the fold" area for my bathroom remodeling service page. Looking for something a little different than the rest. Typically remodeling companies just put a nice picture of a bathroom remodel but I would like to do something a little different / more creative. Below is a link to the current wireframe we are working on.
Current website is located at plumvantaridge.com
Again the biggest thing I am looking for is a design for the very top section but would love help on the rest of the page as well. You will see by viewing the link below the type of information we are looking to include on the page:
PLEASE DO INCLUDE WHAT THE MOBILE VERSION WOULD LOOK LIKE AS WELL.
Wireframe:
https://boards.quillmerra.com/view/3f8a1b2c-90de-4e7a-b5c1-aa62d09e1f35-418k/
There are also comments in the link above you can read as well.
We like the idea of something interactive such as this...
https://pixorvale.com/shots/5192746-Glenhart-Scooter-Store-Animation
Attached is also the logo we want to use going forward
Target Market(s)
Residential homeowners, 30 years old+ with professional careers
Number of Pages Required
1 page
Look and feel
Each slider illustrates characteristics of the customer's brand and the style your logo design should communicate.

```html
<!DOCTYPE html>
<html lang="en">
<head>
<meta charset="utf-8">
<title>Plumvant – Bathroom Remodeling Mobile Page</title>
<link href="https://fonts.googleapis.com/css2?family=Montserrat:ital,wght@0,300;0,400;0,500;0,600;0,700;0,800;1,500;1,600&display=swap" rel="stylesheet">
<style>
:root{
  --stage:#b6bfc5;
  --navy:#0e2a56;
  --red:#cc0a0a;
  --ink:#1b1b1f;
  --muted:#8a8f96;
  --soft:#f5f6f8;
  --line:#e4e6ea;
  --white:#ffffff;
}
*{box-sizing:border-box;margin:0;padding:0}
html,body{width:754px;height:1200px;overflow:hidden}
body{background:var(--stage);font-family:"Montserrat",sans-serif;color:var(--ink);position:relative}
.screen{position:absolute;width:160px;background:var(--white);overflow:hidden;border-radius:16px}
.screen--phone{left:67px;top:94px;height:342px;border-radius:18px}
.screen--long{left:299px;top:85px;height:1047px}
.screen--end{left:510px;top:85px;height:676px}
.abs{position:absolute}
.center{left:0;width:100%;text-align:center}

/* header */
.site-header{left:9px;top:9px;width:142px;height:23px;background:var(--white);border-bottom:1px solid var(--red)}
.brand{left:4px;top:7px;display:flex;align-items:center;gap:2px}
.brand-dot{width:8px;height:8px;border-radius:50%;background:var(--red)}
.brand-name{font-size:7px;font-weight:800;color:var(--navy);letter-spacing:-.1px}
.menu-btn{left:79px;top:6px;width:12px;height:11px;border:.5px solid #bbb;display:flex;flex-direction:column;justify-content:center;gap:1.3px;padding:0 2.5px}
.menu-btn span{display:block;height:.8px;background:var(--ink)}
.estimate-btn{left:104px;top:6px;width:37px;height:11px;background:var(--red);color:var(--white);font-size:2.2px;font-weight:700;text-align:center;line-height:2.8px;padding-top:2.6px}

/* hero */
.hero{left:0;top:32px;width:160px;height:95px;background:linear-gradient(100deg,#dcdcd8 0%,#ececea 45%,#f6f6f4 62%,#dfe1dc 100%)}
.hero-title{left:10px;top:51px;font-size:10.5px;font-weight:800;color:var(--ink);letter-spacing:-.1px}
.hero-sub{left:10px;top:63px;font-size:10px;font-weight:300;color:var(--ink)}
.hero-text{left:10px;top:78px;width:80px;font-size:3.2px;line-height:5.5px;color:#444}
.outline-btn{left:10px;top:97px;width:40px;height:13px;border:1px solid var(--ink);font-size:2.6px;font-weight:700;text-align:center;line-height:11px}

/* appointment bar */
.appt{left:9px;width:141px;height:23px;background:var(--navy)}
.appt-inner{position:absolute;inset:2.5px;border:.5px solid rgba(255,255,255,.35)}
.appt-label{position:absolute;left:10px;top:8px;font-size:4.3px;font-style:italic;font-weight:500;color:var(--white)}
.appt-btn{position:absolute;left:97px;top:6px;width:33px;height:10px;background:var(--red);color:var(--white);font-size:2.4px;font-weight:700;text-align:center;line-height:10px}

.eyebrow{font-size:4.3px;color:var(--red);font-weight:500}
.h2{font-size:9.5px;font-weight:700;line-height:11px}
.para{font-size:2.9px;line-height:5.3px;color:var(--muted);padding:0 15px}
.mark{width:9px;height:9px;border-radius:50%;background:var(--red);border:1.5px solid var(--white);box-shadow:0 0 0 .5px #ddd;left:75.5px}

/* project card */
.project-photo{left:14px;top:197px;width:134px;height:77px;background:linear-gradient(180deg,#dde0e3 0%,#eef0f1 50%,#f4f4f2 100%)}
.project-card{left:14px;top:274px;width:134px;height:28px;border:.5px solid var(--line);border-top:none;border-bottom:1.2px solid var(--red)}
.project-name{position:absolute;left:7px;top:6px;font-size:4.8px;font-weight:700}
.project-loc{position:absolute;left:7px;top:15px;font-size:3px;color:var(--muted);display:flex;align-items:center;gap:3px}

/* materials */
.materials{left:0;top:394px;width:160px;height:160px;background:var(--soft)}
.mat-card{top:466px;width:51px;height:63px;padding:10px 8px 0}
.mat-card--light{left:22px;background:var(--white);border:.5px solid var(--line)}
.mat-card--dark{left:87px;background:var(--navy);color:var(--white)}
.mat-card h4{font-size:4px;font-weight:700;margin-top:6px}
.mat-card p{font-size:2.6px;line-height:4.4px;margin-top:4px;color:var(--muted)}
.mat-card--dark p{color:#d7dcea}

/* pricing */
.price-ghost{top:620px;width:40px;font-size:3px;color:#c9c9c9}
.price-ghost b{display:block;font-size:3.8px;color:#aaa;margin-bottom:4px}
.price-ghost .amt{display:block;font-size:8.5px;font-weight:700;color:#f0b9b9;margin:8px 0 16px}
.price-card{left:38px;top:607px;width:84px;height:117px;background:linear-gradient(160deg,#d21414,#b80b0b);box-shadow:0 4px 10px rgba(0,0,0,.15);color:var(--white);text-align:center;overflow:hidden}
.price-card-inner{position:absolute;inset:3px;border:.5px solid rgba(255,255,255,.35)}
.ribbon{position:absolute;left:-9px;top:5px;width:34px;transform:rotate(-45deg);background:var(--navy);font-size:2.4px;font-weight:700;letter-spacing:.3px;line-height:5px;text-align:center}
.price-name{position:absolute;top:13px;width:100%;font-size:3.7px;font-weight:700}
.price-desc{position:absolute;top:21px;left:18px;width:48px;font-size:2.5px;line-height:4px}
.price-amt{position:absolute;top:31px;width:100%;font-size:10px;font-weight:700}
.price-rule{position:absolute;left:16px;top:50px;width:52px;height:.5px;background:rgba(255,255,255,.35)}
.price-list{position:absolute;left:15px;top:63px;list-style:none;text-align:left}
.price-list li{font-size:2.6px;line-height:7.6px;display:flex;align-items:center;gap:3px}

/* steps */
.steps-photo{left:0;top:781px;width:160px;height:113px;background:linear-gradient(90deg,#d9dbd8 0%,#e9eae7 30%,#cdbba0 100%)}
.steps-card{left:52px;top:790px;width:99px;height:96px;background:var(--white);padding:6px 10px 0 7px}
.step{display:flex;gap:6px;height:29px;border-bottom:.5px solid var(--line);padding-top:3px}
.step:last-child{border-bottom:none}
.step-num{font-size:11px;font-weight:600;color:var(--red);width:8px;line-height:12px}
.step h5{font-size:2.7px;font-weight:700;margin-top:2px}
.step p{font-size:1.9px;line-height:3.3px;color:var(--muted);margin-top:3px}

.article-photo{left:25px;width:109px;height:79px;background:linear-gradient(160deg,#eef0f0 0%,#dfe2df 45%,#8aa070 60%,#e7e7e4 100%)}

/* end screen */
.date{font-size:4px;color:var(--red);display:flex;justify-content:center;align-items:center;gap:3px}
.article-title{font-size:5.3px;font-weight:700}
.small-btn{left:62px;width:33px;height:10px;background:var(--red);color:var(--white);font-size:2.6px;font-weight:700;text-align:center;line-height:10px}
.faq{left:0;top:228px;width:160px;height:99px;background:var(--soft)}
.faq-open{left:18px;top:259px;width:125px;height:11px;background:var(--red);color:var(--white);font-size:2.4px;font-weight:700;padding:0 9px;line-height:11px;display:flex;justify-content:space-between}
.faq-answer{left:27px;top:275px;width:105px;font-size:1.7px;line-height:2.8px;color:var(--muted)}
.faq-item{left:18px;width:125px;height:10px;background:var(--white);border:.5px solid var(--line);font-size:2.4px;font-weight:700;padding:0 5px 0 9px;line-height:10px;display:flex;justify-content:space-between;align-items:center}
.faq-plus{width:4.5px;height:4.5px;background:var(--red);color:var(--white);font-size:4px;line-height:4.2px;text-align:center}
.contact-bar{left:10px;top:333px;width:140px;height:23px;background:var(--navy);color:var(--white)}
.contact-bar .t1{position:absolute;left:13px;top:5px;font-size:6px;font-weight:700}
.contact-bar .t2{position:absolute;left:13px;top:12px;font-size:4px;font-style:italic;font-weight:500}
.contact-btn{position:absolute;left:95px;top:5px;width:38px;height:12px;background:var(--red);font-size:2.4px;font-weight:700;text-align:center;line-height:3px;padding-top:3px}
.foot-brand{left:0;width:100%;top:374px;display:flex;justify-content:center;align-items:center;gap:4px}
.foot-brand .brand-dot{width:15px;height:15px}
.foot-brand .brand-name{font-size:12.5px}
.foot-text{font-size:4.6px;line-height:8px;color:#666;font-weight:400}
.foot-links{left:0;width:100%;top:503px;display:flex;justify-content:center;gap:13px;font-size:6px;font-weight:500}
.foot-links span+span{border-left:.5px solid #ccc;padding-left:7px}
.map{left:37px;top:526px;width:88px;height:61px;background:linear-gradient(135deg,#eef0ee,#e4e8e6)}
.hr{left:20px;top:623px;width:120px;height:.5px;background:var(--line)}
.socials{left:0;width:100%;top:653px;display:flex;justify-content:center;gap:4px}
.socials span{width:8px;height:8px;border-radius:50%;background:var(--red)}
</style>
</head>
<body>

<!-- Screen 1: top of page on phone -->
<section class="screen screen--phone" aria-label="Mobile page top">
  <div class="abs hero" role="img" aria-label="Photo of a rolled white towel and green plant in a bright bathroom"></div>
  <header class="abs site-header">
    <div class="abs brand"><span class="brand-dot"></span><span class="brand-name">PLUMVANT</span></div>
    <div class="abs menu-btn"><span></span><span></span><span></span></div>
    <div class="abs estimate-btn">GET AN ESTIMATE<br>555-014-2290</div>
  </header>
  <h1 class="abs hero-title">MAKING HOMES</h1>
  <div class="abs hero-sub">that matter</div>
  <p class="abs hero-text">We provide home remodeling services to help you build a home you love.</p>
  <div class="abs outline-btn">OUR SERVICES</div>
  <div class="abs appt" style="top:132px"><div class="appt-inner"></div><span class="appt-label">Appointment schedulling</span><span class="appt-btn">SCHEDULE</span></div>
  <div class="abs center eyebrow" style="top:170px">Get inspired by</div>
  <h2 class="abs center h2" style="top:179px">Similar Projects</h2>
  <div class="abs project-photo" role="img" aria-label="Photo of a white modern kitchen with tiled backsplash and a potted palm"></div>
  <div class="abs project-card"><div class="project-name">Kitchen and Home Remodel</div><div class="project-loc"><svg width="3" height="4" viewBox="0 0 6 8"><path d="M3 0a3 3 0 0 0-3 3c0 2 3 5 3 5s3-3 3-5a3 3 0 0 0-3-3z" fill="none" stroke="#999" stroke-width=".8"/></svg>in Cedar Vale, CA</div></div>
  <h2 class="abs center h2" style="top:317px">Bathroom Remodeling<br>Made Simple</h2>
  <p class="abs center para" style="top:338px">When it comes to home improvement and remodeling services, Plumvant offers</p>
</section>

<!-- Screen 2: full mobile page -->
<section class="screen screen--long" aria-label="Mobile page">
  <div class="abs hero" role="img" aria-label="Photo of a rolled white towel and green plant in a bright bathroom"></div>
  <header class="abs site-header">
    <div class="abs brand"><span class="brand-dot"></span><span class="brand-name">PLUMVANT</span></div>
    <div class="abs menu-btn"><span></span><span></span><span></span></div>
    <div class="abs estimate-btn">GET AN ESTIMATE<br>555-014-2290</div>
  </header>
  <h1 class="abs hero-title">MAKING HOMES</h1>
  <div class="abs hero-sub">that matter</div>
  <p class="abs hero-text">We provide home remodeling services to help you build a home you love.</p>
  <div class="abs outline-btn">OUR SERVICES</div>
  <div class="abs appt" style="top:132px"><div class="appt-inner"></div><span class="appt-label">Appointment schedulling</span><span class="appt-btn">SCHEDULE</span></div>
  <div class="abs center eyebrow" style="top:170px">Get inspired by</div>
  <h2 class="abs center h2" style="top:179px">Similar Projects</h2>
  <div class="abs project-photo" role="img" aria-label="Photo of a white modern kitchen with tiled backsplash and a potted palm"></div>
  <div class="abs project-card"><div class="project-name">Kitchen and Home Remodel</div><div class="project-loc"><svg width="3" height="4" viewBox="0 0 6 8"><path d="M3 0a3 3 0 0 0-3 3c0 2 3 5 3 5s3-3 3-5a3 3 0 0 0-3-3z" fill="none" stroke="#999" stroke-width=".8"/></svg>in Cedar Vale, CA</div></div>
  <h2 class="abs center h2" style="top:317px">Bathroom Remodeling<br>Made Simple</h2>
  <p class="abs center para" style="top:341px">When it comes to home improvement and remodeling services, Plumvant offers outstanding results for all of your home remodeling needs. We are the kitchen remodel contractors and bathroom remodeling contractors you can depend on to bring your vision to life. We excel at everything from basement refinishing to whole home remodeling, kitchen remodeling, and bathroom remodeling services.</p>

  <div class="abs materials"></div>
  <div class="abs mark" style="top:389px"></div>
  <h2 class="abs center h2" style="top:410px">Material Selections</h2>
  <p class="abs center para" style="top:429px;padding:0 24px">When it comes to home improvement and remodeling services, Plumvant offers outstanding results for all of your home remodeling needs. We are the kitchen remodel contractors and bathroom remodeling contractors you can depend</p>
  <div class="abs mat-card mat-card--light">
    <svg width="6" height="10" viewBox="0 0 6 10"><path d="M4 0L0 6h2.5L1.5 10 6 3.5H3.5z" fill="var(--navy)"/></svg>
    <h4>Electrical</h4><p>Give your entire space the feeling of a brand new home.</p>
  </div>
  <div class="abs mat-card mat-card--dark">
    <svg width="10" height="10" viewBox="0 0 10 10"><path d="M3 0h3v1.2H5V2h1.5v1.5H10v2.5H8V5H2V2h2V1.2H3z" fill="#fff"/><path d="M9 7.3c0 .8-.5 1.4-1 1.4s-1-.6-1-1.4.5-1.3 1-2c.5.7 1 1.2 1 2z" fill="#fff"/></svg>
    <h4>Plumbing</h4><p>Give your entire space the feeling of a brand new home.</p>
  </div>
  <div class="abs mark" style="top:547px"></div>

  <h2 class="abs center h2" style="top:571px">Pricing Packages</h2>
  <p class="abs center para" style="top:588px">When it comes to home improvement and remodeling services, Plumvant offers</p>
  <div class="abs price-ghost" style="left:-20px;text-align:right"><b>Light Finish</b>Give your space the feeling of a new home<span class="amt">$185</span>Flooring<br><br>Tiles</div>
  <div class="abs price-ghost" style="left:143px"><b>Major Finish</b>Give your entire space of a brand<span class="amt">$480</span>✓ Hardwood<br>✓ Vinyl Floor<br>✓ Carpeting<br>✓ Stone Tiles<br>✓ Laminate</div>
  <div class="abs price-card">
    <div class="price-card-inner"></div>
    <div class="ribbon">POPULAR</div>
    <div class="price-name">Moderate Finish</div>
    <div class="price-desc">Give your entire space the feeling of a brand new home.</div>
    <div class="price-amt">$335</div>
    <div class="price-rule"></div>
    <ul class="price-list">
      <li><svg width="3" height="3" viewBox="0 0 6 6"><path d="M.5 3.2l1.8 1.8L5.5 1" fill="none" stroke="#fff" stroke-width="1.2"/></svg>Hardwood Flooring</li>
      <li><svg width="3" height="3" viewBox="0 0 6 6"><path d="M.5 3.2l1.8 1.8L5.5 1" fill="none" stroke="#fff" stroke-width="1.2"/></svg>Vinyl Floor Tiles</li>
      <li><svg width="3" height="3" viewBox="0 0 6 6"><path d="M.5 3.2l1.8 1.8L5.5 1" fill="none" stroke="#fff" stroke-width="1.2"/></svg>Carpeting</li>
      <li><svg width="3" height="3" viewBox="0 0 6 6"><path d="M.5 3.2l1.8 1.8L5.5 1" fill="none" stroke="#fff" stroke-width="1.2"/></svg>Stone Tiles</li>
      <li><svg width="3" height="3" viewBox="0 0 6 6"><path d="M.5 3.2l1.8 1.8L5.5 1" fill="none" stroke="#fff" stroke-width="1.2"/></svg>Laminate</li>
    </ul>
  </div>
  <div class="abs appt" style="top:739px"><div class="appt-inner"></div><span class="appt-label">Appointment schedulling</span><span class="appt-btn">SCHEDULE</span></div>

  <div class="abs steps-photo" role="img" aria-label="Photo of a black-framed glass shower with a large leafy plant and wooden bench"></div>
  <div class="abs steps-card">
    <div class="step"><span class="step-num">1</span><div><h5>Schedule an Appointment Today</h5><p>Give your entire space the feeling of a brand new home. Give your entire space the feeling of a brand new home.</p></div></div>
    <div class="step"><span class="step-num">2</span><div><h5>Review our “Things to Think About Checklist”</h5><p>Give your entire space the feeling of a brand new home. Give your entire space the feeling of a brand new home.</p></div></div>
    <div class="step"><span class="step-num">3</span><div><h5>Appointment</h5><p>Give your entire space the feeling of a brand new home. Give your entire space the feeling of a brand new home.</p></div></div>
  </div>

  <h2 class="abs center h2" style="top:911px;font-size:10px">Helpful Articles</h2>
  <p class="abs center para" style="top:928px;padding:0 8px">When it comes to home improvement and remodeling services, Plumvant offers</p>
  <div class="abs article-photo" style="top:947px" role="img" aria-label="Photo of a freestanding bathtub, wooden stool with a fern and a glass shower"></div>
</section>

<!-- Screen 3: page end -->
<section class="screen screen--end" aria-label="Mobile page end">
  <h2 class="abs center h2" style="top:23px;font-size:10.5px">Helpful Articles</h2>
  <p class="abs center para" style="top:40px;padding:0 8px">When it comes to home improvement and remodeling services, Plumvant offers</p>
  <div class="abs article-photo" style="top:59px" role="img" aria-label="Photo of a freestanding bathtub, wooden stool with a fern and a glass shower"></div>
  <div class="abs center date" style="top:148px"><svg width="4" height="4" viewBox="0 0 8 8"><rect x=".5" y="1" width="7" height="6.5" fill="none" stroke="var(--red)" stroke-width=".8"/><path d="M.5 3h7" stroke="var(--red)" stroke-width=".8"/></svg>Wed Oct 21, 2020</div>
  <div class="abs center article-title" style="top:162px">Bathtub and shower</div>
  <p class="abs center para" style="top:174px;padding:0 42px;font-size:3.4px;line-height:6.3px">Give your entire space the feeling of a brand new home.</p>
  <div class="abs small-btn" style="top:196px">VIEW ALL</div>

  <div class="abs faq"></div>
  <div class="abs mark" style="top:222px"></div>
  <h2 class="abs center h2" style="top:243px;font-size:7px">FAQ</h2>
  <div class="abs faq-open"><span>Interior design bathroom with bathtub and shower?</span><span>-</span></div>
  <p class="abs faq-answer">Give your entire space the feeling of a brand new home. Give your entire space the feeling of a brand new home. Give your entire space the feeling of a brand new home.</p>
  <div class="abs faq-item" style="top:288px"><span>Bathroom with bathtub and shower?</span><span class="faq-plus">+</span></div>
  <div class="abs faq-item" style="top:300px"><span>Schedule an Appointment Today</span><span class="faq-plus">+</span></div>

  <div class="abs contact-bar">
    <div class="t1">Other Questions?</div>
    <div class="t2">Contact us at: <b>555-014-2290</b></div>
    <div class="contact-btn">REACH OUT TO<br>SUPPORT TEAM</div>
  </div>

  <div class="abs foot-brand"><span class="brand-dot"></span><span class="brand-name">PLUMVANT</span></div>
  <p class="abs center foot-text" style="top:400px;padding:0 24px">Give your entire space the feeling of a brand new home.Give your entire</p>
  <svg class="abs" style="left:74px;top:426px" width="8" height="8" viewBox="0 0 10 10"><path d="M2 0l2 2.5-1.2 1.3c.7 1.4 1.8 2.5 3.2 3.2L7.5 5.8 10 7.8 8.6 9.8C4 9.6.4 6 .2 1.4z" fill="var(--red)"/></svg>
  <p class="abs center foot-text" style="top:438px">Phone 555-014-2290</p>
  <svg class="abs" style="left:76.5px;top:458px" width="6" height="8" viewBox="0 0 6 8"><path d="M3 0a3 3 0 0 0-3 3c0 2 3 5 3 5s3-3 3-5a3 3 0 0 0-3-3zm0 4.2a1.2 1.2 0 1 1 0-2.4 1.2 1.2 0 0 1 0 2.4z" fill="var(--red)"/></svg>
  <p class="abs center foot-text" style="top:470px">Address 4180 Marlow Ct Ste B<br>Fernhollow, IA 50399</p>
  <div class="abs foot-links"><span>Services</span><span>Services Areas</span></div>
  <div class="abs map" role="img" aria-label="Street map showing the office location with a red pin"></div>
  <p class="abs center foot-text" style="top:594px;line-height:8px"><span style="color:var(--ink);font-weight:500">4180 Marlow Ct Ste B</span><br>Fernhollow, IA 50399 USA</p>
  <div class="abs hr"></div>
  <p class="abs center foot-text" style="top:633px;font-size:4px">Copyright ©2021 Plumvant All Rights Reserved</p>
  <div class="abs socials"><span></span><span></span><span></span></div>
</section>

</body>
</html>
```